Talvin Foundation Letterhead

We are a newly established non profit registered in Maryland but operates in Africa, south of the sahara. We offer scholarships to deserving young adults from high school through college. Our color theme for our existing logo is purple, we want a design that is stylish, spellbinding yet a letterhead that projects seriousness. More information on www.thetalvinfoundation.example

Target Market(s)

High school and college students in sub saharan African as well as our donors in the US

Industry/Entity Type

Non Profit

Font styles to use
Script

Requirements
Must have
• Logo at the top and if possible watermark the logo in the middle of the letterhead, contact address,
Should not have
• NA

```html
<!DOCTYPE html>
<html lang="en">
<head>
<meta charset="utf-8">
<title>Talvin Foundation Letterhead</title>
<link href="https://fonts.googleapis.com/css2?family=Cinzel:wght@400&family=Roboto:wght@400&display=swap" rel="stylesheet">
<style>
  :root {
    --purple: #5b2a8c;
    --purple-soft: #8a63b5;
    --ink-grey: #8a8a8e;
    --backdrop: #ececee;
    --paper: #ffffff;
    --watermark: #f1eef5;
  }
  * { margin: 0; padding: 0; box-sizing: border-box; }
  html, body {
    width: 1200px; height: 898px; overflow: hidden;
    background: var(--backdrop);
  }
  .letterhead {
    position: absolute;
    left: 303px; top: 29px;
    width: 594px; height: 840px;
    background: var(--paper);
    box-shadow: 0 6px 24px rgba(0,0,0,0.12);
    overflow: hidden;
  }
  .brand {
    position: absolute; left: 44px; top: 48px;
    width: 220px; text-align: center;
  }
  .brand-mark { display: block; margin: 0 auto 10px; }
  .brand-name {
    font-family: 'Cinzel', serif;
    font-size: 13px; color: var(--purple); letter-spacing: 0.3px;
    line-height: 1.2; white-space: nowrap;
    border-bottom: 1px solid var(--purple-soft);
    padding-bottom: 3px;
  }
  .brand-tagline {
    font-family: 'Roboto', sans-serif;
    font-size: 6px; color: var(--purple); letter-spacing: 1.2px;
    margin-top: 4px; text-transform: uppercase; white-space: nowrap;
  }
  .contact {
    position: absolute; right: 58px; top: 58px;
    list-style: none;
    font-family: 'Roboto', sans-serif; font-size: 9px;
    color: var(--ink-grey); letter-spacing: 0.6px;
  }
  .contact li { display: flex; align-items: center; gap: 8px; margin-bottom: 6px; }
  .contact svg { flex: none; }
  .watermark {
    position: absolute; left: 147px; top: 270px;
  }
  .address {
    position: absolute; left: 0; right: 0; bottom: 44px;
    text-align: center; white-space: nowrap;
    font-family: 'Cinzel', serif; font-size: 9px;
    color: var(--purple); letter-spacing: 1.5px;
  }
  .footer-band {
    position: absolute; left: 0; right: 0; bottom: 0;
    height: 16px; background: var(--purple);
  }
</style>
</head>
<body>
  <main class="letterhead">
    <header class="brand">
      <svg class="brand-mark" width="56" height="56" viewBox="0 0 56 56" aria-hidden="true">
        <circle cx="28" cy="28" r="25" fill="none" stroke="var(--purple-soft)" stroke-width="3"/>
      </svg>
      <div class="brand-name">The Talvin Foundation Inc</div>
      <div class="brand-tagline">Bright futures through learning for all</div>
    </header>

    <ul class="contact">
      <li>
        <svg width="9" height="9" viewBox="0 0 24 24" aria-hidden="true"><path fill="var(--purple)" d="M6.6 10.8a15 15 0 006.6 6.6l2.2-2.2c.3-.3.7-.4 1-.2 1.1.4 2.3.6 3.6.6.6 0 1 .4 1 1V20c0 .6-.4 1-1 1A17 17 0 013 4c0-.6.4-1 1-1h3.5c.6 0 1 .4 1 1 0 1.3.2 2.5.6 3.6.1.3 0 .7-.2 1z"/></svg>
        <span>0207 555 0148</span>
      </li>
      <li>
        <svg width="9" height="9" viewBox="0 0 24 24" aria-hidden="true"><rect x="2" y="5" width="20" height="14" rx="1" fill="none" stroke="var(--purple)" stroke-width="2.5"/><path d="M3 6l9 7 9-7" fill="none" stroke="var(--purple)" stroke-width="2.5"/></svg>
        <span>info@talvinfoundation.example</span>
      </li>
      <li>
        <svg width="9" height="9" viewBox="0 0 24 24" aria-hidden="true"><circle cx="12" cy="12" r="9" fill="none" stroke="var(--purple)" stroke-width="2.5"/><path d="M3 12h18M12 3c3 3 3 15 0 18M12 3c-3 3-3 15 0 18" fill="none" stroke="var(--purple)" stroke-width="2"/></svg>
        <span>www.talvinfoundation.example</span>
      </li>
    </ul>

    <svg class="watermark" width="300" height="300" viewBox="0 0 300 300" aria-hidden="true">
      <circle cx="150" cy="150" r="140" fill="none" stroke="var(--watermark)" stroke-width="14"/>
    </svg>

    <p class="address">Meridian Park Complex, Lindale, Westmark 40210</p>
    <div class="footer-band"></div>
  </main>
</body>
</html>
```